Meridian Rest Supply Needs Business Card

Looking for a very nice looking business card. Creative but not extravagant. We sell beds and pillows across the U.S. and need something professional but catchy. I have attached the logo.

Name : Dale Fenwick
Title : President
Phone : (800) 417-2964
Email: sleep@quorvana.com
Website: www.quorvana.com

Can be single-sided or double-sided
horizontal or vertical

Can use Blues/Greys

Target Market(s)

Mass Market

Industry/Entity Type

Retail

Contact Information for Business Card

Name : Dale Fenwick
Title : President
Phone : (800) 417-2964
Email: sleep@quorvana.com
Website: www.quorvana.com

Requirements
Must have
• Clean, Modern, Smooth
• Can use Blues/Greys
• On the other side without the information - have something simple like www.quorvana.com or our logo
Nice to have
• Surprise me
Should not have
• Nothing crazy, nothing cluttered

```html
<!DOCTYPE html>
<html lang="en">
<head>
<meta charset="utf-8">
<title>Quorvana Business Card</title>
<link href="https://fonts.googleapis.com/css2?family=Open+Sans:wght@400;700&display=swap" rel="stylesheet">
<style>
  :root {
    --bg: #23262d;
    --blue: #35bce8;
    --white: #ffffff;
    --ink: #4a4a4f;
    --rule: #555559;
    --g1: #4b4b50;
    --g2: #66666b;
    --g3: #7f8084;
    --g4: #98999d;
    --g5: #b1b3b6;
    --g6: #cacbce;
    --g7: #e4e5e7;
  }
  * { box-sizing: border-box; margin: 0; padding: 0; }
  html, body { width: 1200px; height: 1200px; overflow: hidden; }
  body {
    background: var(--bg);
    font-family: "Open Sans", sans-serif;
    display: flex;
    flex-direction: column;
    align-items: center;
    justify-content: center;
    gap: 80px;
  }
  .card {
    position: relative;
    width: 760px;
    height: 434px;
    overflow: hidden;
  }
  /* Front */
  .card-front { background: var(--white); }
  .contact {
    position: absolute;
    left: 44px;
    top: 52px;
    color: var(--ink);
  }
  .contact-name {
    color: var(--blue);
    font-weight: 700;
    font-size: 17px;
    letter-spacing: 0.3px;
    text-transform: uppercase;
  }
  .contact-title { font-size: 16px; margin-top: -2px; }
  .contact-line {
    display: flex;
    align-items: center;
    gap: 8px;
    font-size: 13px;
    margin-top: 4px;
  }
  .contact-line svg { width: 11px; height: 11px; fill: var(--blue); }
  .contact-title + .contact-line { margin-top: 8px; }
  .divider {
    position: absolute;
    left: 200px;
    right: 40px;
    top: 107px;
    height: 1.5px;
    background: var(--rule);
  }
  .brand {
    position: absolute;
    display: flex;
    align-items: center;
    color: var(--blue);
    font-weight: 700;
    line-height: 1;
  }
  .brand-dot {
    flex: none;
    border-radius: 50%;
    background: var(--blue);
  }
  .brand-front {
    right: 60px;
    top: 150px;
    gap: 16px;
    font-size: 60px;
  }
  .brand-front .brand-dot { width: 28px; height: 28px; }
  .band {
    position: absolute;
    left: 0; right: 0; bottom: 0;
    height: 66px;
    display: flex;
  }
  .band span { flex: 1; }
  .band .end { flex: 0 0 20px; background: var(--blue); }
  .website {
    position: absolute;
    left: 70px;
    bottom: 20px;
    color: var(--white);
    font-weight: 700;
    font-size: 17px;
    letter-spacing: 9px;
  }
  /* Back */
  .card-back {
    background: var(--blue);
    padding: 24px;
  }
  .stripes {
    position: relative;
    width: 100%;
    height: 100%;
    display: flex;
  }
  .stripes span { flex: 1; }
  .s1 { background: var(--g1); }
  .s2 { background: var(--g2); }
  .s3 { background: var(--g3); }
  .s4 { background: var(--g4); }
  .s5 { background: var(--g5); }
  .s6 { background: var(--g6); }
  .s7 { background: var(--g7); }
  .brand-back {
    left: 50%;
    top: 50%;
    transform: translate(-50%, -50%);
    gap: 20px;
    font-size: 76px;
  }
  .brand-back .brand-dot { width: 34px; height: 34px; }
</style>
</head>
<body>
  <section class="card card-front">
    <div class="contact">
      <p class="contact-name">Dale Fenwick</p>
      <p class="contact-title">President</p>
      <p class="contact-line">
        <svg viewBox="0 0 12 12"><path d="M1 4c0-2 2-3 5-3s5 1 5 3v1H8V4H4v1H1zM2 6h8l1 5H1z"/></svg>
        (800) 417-2964
      </p>
      <p class="contact-line">
        <svg viewBox="0 0 12 12"><path d="M1 3h10v7H1zM1 3l5 4 5-4" /></svg>
        sleep@quorvana.com
      </p>
    </div>
    <div class="divider"></div>
    <p class="brand brand-front"><span class="brand-dot"></span>Quorvana</p>
    <div class="band">
      <span class="end"></span>
      <span class="s1"></span><span class="s2"></span><span class="s3"></span>
      <span class="s4"></span><span class="s5"></span><span class="s6"></span>
      <span class="s7"></span>
      <span class="end"></span>
    </div>
    <p class="website">www.quorvana.com</p>
  </section>

  <section class="card card-back">
    <div class="stripes">
      <span class="s1"></span><span class="s2"></span><span class="s3"></span>
      <span class="s4"></span><span class="s5"></span><span class="s6"></span>
      <span class="s7"></span>
      <p class="brand brand-back"><span class="brand-dot"></span>Quorvana</p>
    </div>
  </section>
</body>
</html>
```